web page layout, style , color, font & flow design

We are developing a single page application. The SPA (single page application) will display natural gas pipeline flow data once the customer logs on. The customer has a choice of the region, the pipeline, the zone on the pipeline, whether the point is a delivery point or receipt point and the state the pipeline flows through.
we have jumpstarted the project and are attaching a pdf of the same.

we are using mockingbird for the wireframe. any designer is free to use this tool to make changes.

A mockingbird wireframe link is added below. you are free to use it and to make changes. please save the changed wireframe in a different name

we are looking for inputs on layout, style , color, font & flow.

A logo jpg file has also been attached.

Target Market(s)

this single web page is going to be used by natural gas traders and schedulers day in and day out. the application is more of business to business corporate application.

Industry/Entity Type

Delivery

Requirements
Must have
• layout ,flow, size, color, font , ease of use.

```html
<!DOCTYPE html>
<html lang="en">
<head>
<meta charset="utf-8">
<title>Gasflow Supply Desk</title>
<link href="https://fonts.googleapis.com/css2?family=Open+Sans:wght@400;600;700&display=swap" rel="stylesheet">
<style>
:root{
  --page-top:#34435a;
  --page-bottom:#151c27;
  --brand:#4b72a0;
  --brand-dark:#3b5c84;
  --tab-idle:#9c9c9c;
  --tab-rest:#dadada;
  --panel:#ffffff;
  --sidebar:#f6f6f6;
  --rule:#e3e3e3;
  --text:#444a52;
  --muted:#6b7178;
  --head-bg:#f1f1f1;
  --page-btn:#8a8a8a;
  --page-active:#2c3e55;
  --white:#ffffff;
}
*{box-sizing:border-box;margin:0;padding:0}
html,body{width:1200px;height:775px;overflow:hidden}
body{
  position:relative;
  font-family:"Open Sans",Arial,sans-serif;
  color:var(--text);
  background:linear-gradient(180deg,var(--page-top) 0%,var(--page-bottom) 100%);
}
.app{position:absolute;left:98px;top:22px;width:1004px;height:703px;background:var(--panel)}
.topbar{height:41px;background:var(--brand);border-bottom:3px solid var(--brand-dark);display:flex;align-items:center;position:relative}
.brand{display:flex;align-items:center;padding-left:10px;color:var(--white);font-weight:700;font-size:14px}
.brand-mark{width:26px;height:26px;border-radius:50%;background:var(--white);margin-right:10px}
.menu-icon{margin-left:14px}
.topbar-search{position:absolute;left:773px;top:0;width:47px;height:38px;border-left:1px solid var(--brand-dark);display:flex;align-items:center;justify-content:center}
.user{position:absolute;left:820px;top:0;height:38px;border-left:1px solid var(--brand-dark);display:flex;align-items:center;padding-left:10px;color:var(--white);font-size:14px}
.avatar{width:30px;height:30px;border-radius:50%;background:linear-gradient(180deg,#d9dde2,#9aa6b3);margin-right:10px}
.user svg{margin-left:8px}
.tabs{display:flex;gap:3px;padding:7px 5px 0 5px;height:39px}
.tab{width:112px;height:32px;background:var(--tab-idle);color:var(--white);font-weight:600;font-size:13px;display:flex;align-items:center;justify-content:center}
.tab.is-active{background:var(--brand)}
.tab-fill{flex:1;height:32px;background:var(--tab-rest)}
.sidebar{position:absolute;left:0;top:86px;width:243px;bottom:0;background:var(--sidebar);list-style:none}
.sidebar li{height:36px;border-bottom:1px solid var(--rule);display:flex;align-items:center;padding-left:28px;font-size:12.5px;color:var(--text);position:relative}
.sidebar li::before{content:"";position:absolute;left:15px;top:15px;width:5px;height:5px;border-left:1px solid var(--muted);border-bottom:1px solid var(--muted);transform:rotate(45deg)}
.content{position:absolute;left:274px;top:111px;width:700px}
.filters{display:flex;gap:5px;height:32px;position:relative}
.select{width:150px;height:32px;border:1px solid #c9c9c9;border-radius:3px;font-size:12px;display:flex;align-items:center;padding-left:11px;position:relative;background:var(--white)}
.select::after{content:"";position:absolute;right:10px;top:10px;border-left:3px solid transparent;border-right:3px solid transparent;border-bottom:4px solid #555}
.select::before{content:"";position:absolute;right:10px;top:17px;border-left:3px solid transparent;border-right:3px solid transparent;border-top:4px solid #555}
.gas-updates{position:absolute;left:551px;top:0;z-index:2}
.dropdown{position:absolute;left:551px;top:32px;width:150px;background:var(--white);border:1px solid #c9c9c9;z-index:2;list-style:none;font-size:12px}
.dropdown li{height:31px;display:flex;align-items:center;padding-left:11px;border-bottom:1px solid #d4d4d4}
.dropdown li:last-child{border-bottom:none}
.flow-table{margin-top:23px;width:700px;border-collapse:collapse;border:1px solid #d4d4d4;font-size:11px;table-layout:fixed}
.flow-table th{height:50px;background:linear-gradient(180deg,#f7f7f7,#e9e9e9);font-weight:400;font-size:13px;color:var(--text);border-right:1px solid #d8d8d8}
.flow-table td{height:43px;text-align:center;border-right:1px solid #e2e2e2;border-top:1px solid #e2e2e2;background:linear-gradient(180deg,#ffffff,#f5f5f5)}
.pager{display:flex;justify-content:flex-end;gap:4px;margin-top:16px;align-items:center}
.pager span{min-width:20px;height:20px;background:var(--page-btn);color:var(--white);font-size:10px;display:flex;align-items:center;justify-content:center;border-radius:2px;padding:0 4px}
.pager span.is-current{background:var(--page-active)}
.pager span.gap{background:none;color:var(--muted);min-width:14px}
.footer{position:absolute;left:0;top:742px;width:1200px;text-align:center;color:var(--white);font-size:11px}
</style>
</head>
<body>
<div class="app">
  <header class="topbar">
    <div class="brand"><span class="brand-mark"></span>Gasflow Supply Desk
      <svg class="menu-icon" width="12" height="11" viewBox="0 0 12 11"><rect y="0" width="12" height="2" fill="#fff"/><rect y="4.5" width="12" height="2" fill="#fff"/><rect y="9" width="12" height="2" fill="#fff"/></svg>
    </div>
    <div class="topbar-search"><svg width="14" height="14" viewBox="0 0 14 14"><circle cx="5.5" cy="5.5" r="4" fill="none" stroke="#fff" stroke-width="2"/><line x1="8.5" y1="8.5" x2="13" y2="13" stroke="#fff" stroke-width="2.4"/></svg></div>
    <div class="user"><span class="avatar" role="img" aria-label="User profile photo"></span>Marcus Hale Re
      <svg width="14" height="14" viewBox="0 0 14 14"><circle cx="7" cy="7" r="4.5" fill="none" stroke="#fff" stroke-width="3" stroke-dasharray="2.2 1.3"/><circle cx="7" cy="7" r="2.6" fill="none" stroke="#fff" stroke-width="1.6"/></svg>
    </div>
  </header>
  <nav class="tabs">
    <div class="tab is-active">NorthEast</div><div class="tab">MidWest</div><div class="tab">SouthEast</div><div class="tab">SouthWest</div><div class="tab">Central</div><div class="tab">West</div><div class="tab-fill"></div>
  </nav>
  <ul class="sidebar">
    <li>Alderbrook</li><li>CRT</li><li>Dunmore</li><li>Eastern Bay NG</li><li>East Ridge NG</li><li>Summit Gas</li><li>Equiline Inc</li><li>Fieldstone Gas</li><li>Ironwood</li><li>Harborline &amp; North East</li><li>Meridian Pipeline</li><li>Northfield Fuel Gas Supply Corp</li><li>Porter NG</li><li>St. Clair Gas</li><li>Tanner Gas</li><li>Tevco</li><li>Tranlo</li>
  </ul>
  <main class="content">
    <div class="filters">
      <div class="select">Location Type</div>
      <div class="select">States</div>
      <div class="select">Zones</div>
      <div class="select gas-updates">Gas Updates</div>
    </div>
    <ul class="dropdown"><li>Timely</li><li>Evening</li><li>Interday1</li></ul>
    <table class="flow-table">
      <colgroup><col style="width:89px"><col style="width:91px"><col style="width:110px"><col style="width:82px"><col style="width:74px"><col style="width:86px"><col style="width:82px"><col style="width:86px"></colgroup>
      <thead><tr><th>Gasday</th><th>Location</th><th>Location Name</th><th>Flow_Ind</th><th>Loc_Desc</th><th>Op_cap</th><th>Sched_cap</th><th>Op_avail_cap</th></tr></thead>
      <tbody>
        <tr><td>Item 3</td><td>Item 3</td><td>DUNMORE..</td><td>Delivery</td><td>DPQ</td><td>5,47,181</td><td>1,050</td><td>10,500</td></tr>
        <tr><td>Item 5</td><td>Item 2</td><td>COLTON..</td><td>Delivery</td><td>DPQ</td><td>4,41,824</td><td>805</td><td>4805</td></tr>
        <tr><td>Item 7</td><td>Item 1</td><td>INDIGO..</td><td>Delivery</td><td>DPQ</td><td>5,402</td><td>402</td><td>4020</td></tr>
        <tr><td>Item 8</td><td>Item 6</td><td>INDIGO..</td><td>Delivery</td><td>DPQ</td><td>63,989</td><td>3,989</td><td>989</td></tr>
        <tr><td>Item 11</td><td>Item 8</td><td>EQUILINE..</td><td>Delivery</td><td>DPQ</td><td>5,402</td><td>2</td><td>200</td></tr>
        <tr><td>Item 15</td><td>Item 9</td><td>NORTHFLD..</td><td>Delivery</td><td>DPQ</td><td>55,588</td><td>788</td><td>88</td></tr>
        <tr><td>Item 17</td><td>Item 10</td><td>NORTHFLD..</td><td>Delivery</td><td>DPQ</td><td>24,228</td><td>4,228</td><td>4,228</td></tr>
        <tr><td>Item 15</td><td>Item 9</td><td>NORTHFLD..</td><td>Delivery</td><td>DPQ</td><td>55,588</td><td>788</td><td>88</td></tr>
        <tr><td>Item 17</td><td>Item 10</td><td>NORTHFLD..</td><td>Delivery</td><td>DPQ</td><td>24,228</td><td>4,228</td><td>4,228</td></tr>
        <tr><td>Item 15</td><td>Item 9</td><td>NORTHFLD..</td><td>Delivery</td><td>DPQ</td><td>55,588</td><td>788</td><td>88</td></tr>
      </tbody>
    </table>
    <div class="pager">
      <span>&#8249;</span><span>1</span><span class="is-current">2</span><span>3</span><span>4</span><span>5</span><span class="gap">...</span><span>10</span><span>20</span><span>30</span><span>&#8250;</span>
    </div>
  </main>
</div>
<footer class="footer">&copy; 2014 Gasflow Supply Desk. All Rights Reserved</footer>
</body>
</html>
```